Home based bath & shave business wants to redesign labels

I would like to have new labels designed to fit the body lotion and bath oil bottles. We want them similar but different. The key ingredient for all of Ferrucci's Bath & Shave products is olive oil.

You are free to change colors. I have attached our logo and current labels. The current labels just don't look right to me (pictures attached). I like the script font, but am willing to entertain another. I have our logo in several formats and the font, should you want it.

Target Market(s)

Women

Industry/Entity Type

Business

Font styles to use
Decorative
Script

Requirements
Must have
• Both product labels must include our logo.The logo must stay the same though to make it work with the label, you can change the color if needed.
• It should be a vertical label.
• The bottle used is a 8 oz Clear PET Tapered Naples Oval Bottle (I have attached pictures) and its dimensions are:
• Length 2.548 in / 6.472 cm
• Width 1.479 in / 3.757 cm
• Height 6.639 in / 16.863 cm

```html
<!DOCTYPE html>
<html lang="en">
<head>
<meta charset="utf-8">
<title>Ferrucci's Bath &amp; Shave – Labels</title>
<link rel="stylesheet" href="https://fonts.googleapis.com/css2?family=Pinyon+Script&family=Open+Sans:wght@400&display=swap">
<style>
  :root{
    --page:#ffffff;
    --frame:#f09a2a;
    --lotion-pink:#e777c6;
    --lotion-pink-deep:#d95fb4;
    --cream:#efe6d2;
    --olive:#5f7d1e;
    --leaf-light:#a9d13b;
    --leaf-mid:#5f9b1c;
    --leaf-dark:#2f5a12;
    --brand-red:#e0262c;
    --white:#ffffff;
  }
  *{margin:0;padding:0;box-sizing:border-box}
  html,body{width:1200px;height:1000px;overflow:hidden;background:var(--page)}
  .canvas{position:relative;width:1200px;height:1000px;background:var(--page)}

  .label{
    position:absolute;top:313px;width:243px;height:415px;
    border:3px solid var(--frame);overflow:hidden;
  }
  .label--lotion{left:172px;background:var(--lotion-pink)}
  .label--oil{left:765px}

  .label__scene{position:absolute;inset:0;
    background:
      radial-gradient(ellipse at 30% 90%, #6d4a5e 0%, transparent 35%),
      linear-gradient(180deg,var(--leaf-light) 0%,var(--leaf-mid) 45%,var(--leaf-dark) 100%);
  }

  .brand-box{
    position:absolute;left:33px;top:-3px;width:170px;height:120px;
    background:var(--white);border:3px solid var(--frame);border-top:none;
    border-radius:0 0 26px 26px;
    display:flex;align-items:center;justify-content:center;text-align:center;
  }
  .brand-name{
    font-family:"Pinyon Script",cursive;font-weight:400;
    color:var(--brand-red);font-size:25px;line-height:1.05;
  }

  .product-title{
    position:absolute;left:0;right:0;top:164px;text-align:center;
    font-family:"Pinyon Script",cursive;font-size:36px;color:var(--white);
  }
  .rule{position:absolute;left:24px;right:24px;height:1px;background:var(--white);opacity:.85}
  .rule--top{top:160px;left:60px;right:60px}
  .rule--bottom{top:214px}

  .lotion-photo{
    position:absolute;left:0;right:0;top:215px;height:162px;
    background:
      radial-gradient(ellipse at 30% 35%, var(--olive) 0%, transparent 22%),
      radial-gradient(ellipse at 65% 50%, var(--olive) 0%, transparent 16%),
      linear-gradient(180deg,var(--lotion-pink) 0%,var(--cream) 35%,#f7f1e4 100%);
  }
  .label--lotion .ingredients{
    position:absolute;left:10px;right:10px;top:378px;
    font-family:"Open Sans",sans-serif;font-size:4.6px;line-height:1.45;
    color:var(--brand-red);text-align:center;
  }
  .label--lotion .lotion-base{position:absolute;left:0;right:0;top:377px;bottom:0;background:#f7f1e4}

  .label--oil .ingredients{
    position:absolute;left:8px;right:8px;top:390px;
    font-family:"Open Sans",sans-serif;font-size:6.4px;color:var(--white);
  }
</style>
</head>
<body>
<div class="canvas">

  <section class="label label--lotion">
    <div class="brand-box"><span class="brand-name">Ferrucci's<br>Bath &amp; Shave</span></div>
    <span class="rule rule--top"></span>
    <h1 class="product-title">Body Lotion</h1>
    <span class="rule rule--bottom"></span>
    <div class="lotion-photo" role="img" aria-label="Photo of green olives and olive oil splashing into creamy lotion"></div>
    <div class="lotion-base"></div>
    <p class="ingredients">Ingredients: Water, Olive Oil, Aloe Vera Juice, Avocado Oil, Rice Bran Oil, BTMS-50, Glycerin, Stearyl Alcohol, Oat Extract, DL Panthenol, Optiphen, Buckthorn Extract, Vitamin E and Fragrance oil.</p>
  </section>

  <section class="label label--oil">
    <div class="label__scene" role="img" aria-label="Photo of green olive tree leaves and buds with ripe olives along the bottom"></div>
    <div class="brand-box"><span class="brand-name">Ferrucci's<br>Bath &amp; Shave</span></div>
    <span class="rule rule--top"></span>
    <h1 class="product-title">Bath Oil</h1>
    <span class="rule rule--bottom"></span>
    <p class="ingredients">Ingredients: olive oil, Grapeseed oil and fragrance oil.</p>
  </section>

</div>
</body>
</html>
```